Harbourline Plumbing business card full re design & logo design

Harbourline Plumbing is a Sydney based mechanical plumbing contractor company.
We would like a full redesign with new logo etc which we can take to a future website, uniforms, vehicle sign writing etc.
Blue is my preferred choice of colour but i would be open to see a couple of alternatives thrown in the mix to see how they compare. I am open to see on white cards, black cards etc. Open to many new ideas.
Please see attached original business cards which have been used for the last 5 years.

Target Market(s)

Mechanical services industry.

Industry/Entity Type

Plumbing

Contact Information for Business Card

Colin Ashdale
Director

Mob: 0427 590 614
Email: colin@harbourlineplumbing.net.au
PO BOX 816
Merrowdale NSW 2159
Lic: 583106k

Logo Text

Harbourline Plumbing

Font styles to use
Sans Serif

Colors
0655a3
3276b5
0792cd
33a6d7
85cae6
000000
333333
474747

Requirements
Must have
• Things that make it very professional and very well presented.
Nice to have
• Same description or very similar to attached uploaded file
Should not have
• Anything that makes it look unprofessional or cartoony.

```html
<!DOCTYPE html>
<html lang="en">
<head>
<meta charset="utf-8">
<title>Harbourline Plumbing – Business Card</title>
<link href="https://fonts.googleapis.com/css2?family=Montserrat:wght@500;700&family=Work+Sans:wght@400;500&display=swap" rel="stylesheet">
<style>
  :root {
    --blue-deep: #0655a3;
    --blue: #0792cd;
    --blue-mid: #3276b5;
    --charcoal: #333333;
    --graphite: #474747;
    --ink: #000000;
    --paper: #ffffff;
    --backdrop: #e9e9e7;
    --muted: #9a9a9a;
  }
  * { box-sizing: border-box; margin: 0; padding: 0; }
  html, body { width: 1200px; height: 930px; overflow: hidden; }
  body {
    background: var(--backdrop);
    position: relative;
    font-family: "Work Sans", sans-serif;
  }
  .card {
    position: absolute;
    width: 620px;
    height: 354px;
    border-radius: 18px;
    overflow: hidden;
    box-shadow: 0 6px 18px rgba(0,0,0,.18);
  }
  /* Back of card */
  .card-back { left: 60px; top: 70px; background: var(--charcoal); color: var(--paper); }
  .card-back .headline {
    position: absolute; top: 44px; left: 0; right: 0; text-align: center;
    font-family: "Montserrat", sans-serif; font-weight: 500;
    font-size: 20px; letter-spacing: 2px;
  }
  .brand {
    position: absolute; display: flex; align-items: center; gap: 10px;
    font-family: "Montserrat", sans-serif; font-weight: 700;
    color: var(--blue); letter-spacing: 1px; line-height: 1.05;
  }
  .brand-dot { width: 34px; height: 34px; border-radius: 50%; background: var(--blue); flex: none; }
  .card-back .brand { left: 48px; top: 150px; font-size: 24px; }
  .divider-back {
    position: absolute; left: 328px; top: 118px; width: 1px; height: 110px;
    background: var(--muted);
  }
  .services {
    position: absolute; left: 352px; top: 116px; list-style: none;
    font-size: 15px; line-height: 19px;
  }
  .services li { display: flex; align-items: center; gap: 8px; }
  .drop { width: 7px; height: 7px; border-radius: 50%; background: var(--blue); flex: none; }
  .card-back .tagline {
    position: absolute; bottom: 40px; left: 0; right: 0; text-align: center;
    font-size: 19px; letter-spacing: 1px;
  }
  /* Front of card */
  .card-front { left: 520px; top: 506px; background: var(--paper); color: var(--ink); }
  .card-front .brand { left: 36px; top: 150px; font-size: 22px; }
  .divider-front {
    position: absolute; left: 296px; top: 90px; width: 1px; height: 150px;
    background: var(--blue);
  }
  .contact {
    position: absolute; left: 316px; right: 14px; top: 82px;
    font-size: 15px; line-height: 22px; white-space: nowrap;
  }
  .contact .name {
    font-family: "Montserrat", sans-serif; font-weight: 700; font-size: 21px;
    color: var(--blue); line-height: 28px;
  }
  .contact .row { display: flex; align-items: center; gap: 6px; }
  .contact .row svg { width: 13px; height: 13px; flex: none; }
  .contact .licence { margin-top: 6px; }
  .contact .licence span { color: var(--blue); }
  .edge-band { position: absolute; left: 0; bottom: 0; width: 620px; height: 26px; }
</style>
</head>
<body>

  <section class="card card-back">
    <p class="headline">MECHANICAL PLUMBING SERVICES</p>
    <div class="brand"><span class="brand-dot"></span><span>HARBOURLINE<br>PLUMBING</span></div>
    <div class="divider-back"></div>
    <ul class="services">
      <li><span class="drop"></span>Paint Correction</li>
      <li><span class="drop"></span>Exterior detailing</li>
      <li><span class="drop"></span>Interior Detailing</li>
      <li><span class="drop"></span>Engine Bay Detailing</li>
      <li><span class="drop"></span>Headlight restoration</li>
      <li><span class="drop"></span>Ceramic Coatings</li>
    </ul>
    <p class="tagline">HARBOURLINE have the SOLUTION</p>
  </section>

  <section class="card card-front">
    <div class="brand"><span class="brand-dot"></span><span>HARBOURLINE<br>PLUMBING</span></div>
    <div class="divider-front"></div>
    <div class="contact">
      <p class="name">COLIN ASHDALE</p>
      <p>Director</p>
      <p>PO BOX 816</p>
      <p>Merrowdale NSW 2159</p>
      <p class="row">
        <svg viewBox="0 0 16 16" aria-hidden="true"><path fill="#0792cd" d="M3.6 1.5l2.3 2.8-1.3 1.6c.9 2 2.5 3.6 4.5 4.5l1.6-1.3 2.8 2.3-1.5 2.1C6.8 13.3 2.7 9.2 1.5 3z"/></svg>
        0427 590 614
      </p>
      <p class="row">
        <svg viewBox="0 0 16 16" aria-hidden="true"><rect x="1.5" y="3.5" width="13" height="9" fill="none" stroke="#0792cd" stroke-width="1.5"/><path d="M1.5 3.5L8 9l6.5-5.5" fill="none" stroke="#0792cd" stroke-width="1.5"/></svg>
        colin@harbourlineplumbing.net.au
      </p>
      <p class="licence"><span>Lic:</span> 583106k</p>
    </div>
    <svg class="edge-band" viewBox="0 0 620 26" preserveAspectRatio="none" aria-hidden="true">
      <polygon points="0,0 395,0 386,26 0,26" fill="#333333"/>
      <polygon points="401,0 620,0 620,26 392,26" fill="#0792cd"/>
    </svg>
  </section>

</body>
</html>
```